Sydney law firm, Prestwicks Solicitors, needs a flyer design!

We need a flyer design for our law firm which has been operating in Sydney for over 35 years. We want to send the flyer out to potential clients and also to existing clients to let them know the range of services that we provide. Our corporate colours are white, red and black and we would like these incorporated somewhat. The final design should be clean, modern and professional.

We would like the design to fit a double sided flyer approx. 210mm high x 100mm wide.

Industry/Entity Type

Law Firm

Font styles to use
Serif
Sans Serif

Colors
eb2026
ffffff

Requirements
Must have
• Details needed on the flyer are:
• Prestwicks Solicitors
• 3/82 Carradine Street, Liverpool, NSW 2170
• (02) 9418 3562
• www.prestwickssolicitors-example.com.au
• info@prestwickssolicitors-example.com.au
• Our areas of practice include:
• Property Law
• Conveyancing
• Leases
• Criminal Law
• Family Law
• Litigation and Dispute Resolution
• Company Law
• Wills and Estates
• Powers of Attorney and Guardianship
Should not have
• a picture of scales or a picture of a gavel

```html
<!DOCTYPE html>
<html lang="en">
<head>
<meta charset="utf-8">
<title>Prestwicks Solicitors – Flyer</title>
<link rel="stylesheet" href="https://fonts.googleapis.com/css2?family=Cinzel:wght@400&family=Montserrat:wght@400;500;800&display=swap">
<style>
  :root {
    --backdrop: #2a2b2e;
    --red: #eb2026;
    --black: #000000;
    --white: #ffffff;
    --ink: #231f20;
    --grey-panel: #e4e4e6;
    --rule: #9a9a9c;
  }
  html, body {
    margin: 0;
    width: 1200px;
    height: 1043px;
    overflow: hidden;
    background: var(--backdrop);
    font-family: "Montserrat", Arial, sans-serif;
  }
  .flyer {
    position: absolute;
    top: 69px;
    width: 430px;
    height: 902px;
    background: var(--black);
    overflow: hidden;
  }
  .flyer--front { left: 168px; }
  .flyer--back { left: 628px; }

  /* Front */
  .handshake-photo {
    position: absolute;
    left: 0; top: 0;
    width: 430px; height: 354px;
    background: linear-gradient(135deg, #1c1c1c 0%, #6f6a66 45%, #cfcac5 70%, #3a3836 100%);
  }
  .intro {
    position: absolute;
    left: 46px; top: 386px;
    width: 338px;
    color: var(--white);
  }
  .intro__heading {
    margin: 0 0 14px -10px;
    width: 358px;
    text-align: center;
    color: var(--red);
    font-weight: 800;
    font-size: 15.5px;
    line-height: 23px;
  }
  .intro__text {
    margin: 0 0 21px;
    font-size: 14.2px;
    line-height: 21px;
    text-align: justify;
  }

  /* Back */
  .services-header {
    position: absolute;
    left: 0; top: 0;
    width: 430px; height: 240px;
    background: var(--red);
  }
  .services-header__title {
    margin: 0;
    padding-top: 28px;
    text-align: center;
    font-family: "Cinzel", "Times New Roman", serif;
    font-weight: 400;
    font-size: 66px;
    line-height: 60px;
    color: var(--white);
  }
  .services-panel {
    position: absolute;
    left: 0; top: 240px;
    width: 430px; height: 424px;
    background: linear-gradient(90deg, #f1f1f2 0%, var(--grey-panel) 100%);
  }
  .column-photo {
    position: absolute;
    right: 0; top: 0;
    width: 210px; height: 424px;
    background: linear-gradient(90deg, rgba(228,228,230,0) 0%, #cfcfd1 25%, #f4f4f4 55%, #b9b9bb 100%);
  }
  .service-list {
    position: absolute;
    left: 57px; top: 24px;
    width: 176px;
    margin: 0; padding: 0;
    list-style: none;
  }
  .service-list__item {
    position: relative;
    font-size: 18.5px;
    line-height: 25px;
    color: var(--ink);
    padding-bottom: 12.5px;
  }
  .service-list__item::after {
    content: "";
    position: absolute;
    left: 0; bottom: 6px;
    width: 176px; height: 1px;
    background: var(--rule);
  }
  .service-list__item::before {
    content: "";
    position: absolute;
    left: 0; bottom: 5px;
    width: 39px; height: 3px;
    background: var(--red);
    z-index: 1;
  }
  .service-list__item:last-child::before,
  .service-list__item:last-child::after { display: none; }

  /* Shared contact block */
  .contact-block {
    position: absolute;
    left: 0; top: 664px;
    width: 430px; height: 215px;
    background: var(--white);
    text-align: center;
    color: var(--ink);
  }
  .firm-name {
    margin: 30px 0 0;
    font-family: "Cinzel", "Times New Roman", serif;
    font-weight: 400;
    font-size: 27px;
    line-height: 50px;
    letter-spacing: 1px;
    color: var(--ink);
  }
  .contact-block__address {
    margin: 26px 0 0;
    font-size: 14px;
    line-height: 18px;
  }
  .contact-block__phone {
    margin: 10px 0 0;
    font-weight: 800;
    font-size: 21px;
    line-height: 28px;
  }
  .contact-block__link {
    margin: 0;
    font-size: 14px;
    line-height: 18px;
  }
</style>
</head>
<body>
  <section class="flyer flyer--front">
    <div class="handshake-photo" role="img" aria-label="Black and white photograph of two business people shaking hands"></div>
    <div class="intro">
      <h2 class="intro__heading">Established For Over 30 Years,<br>You Can Feel Confident With Our Team</h2>
      <p class="intro__text">Prestwicks Solicitors is a private law firm based in Liverpool that has been servicing the Sydney area for over 30 years. With a dedicated, professional and friendly team we pride ourselves on delivering an exceptional legal service to our clients.</p>
      <p class="intro__text">Offering a complete legal service at affordable rates, our clients really do come first.</p>
    </div>
    <div class="contact-block">
      <p class="firm-name">PRESTWICKS SOLICITORS</p>
      <p class="contact-block__address">3/82 Carradine Street, Liverpool, NSW 2170</p>
      <p class="contact-block__phone">(02) 9418 3562</p>
      <p class="contact-block__link">www.prestwickssolicitors-example.com.au</p>
      <p class="contact-block__link">info@prestwickssolicitors-example.com.au</p>
    </div>
  </section>

  <section class="flyer flyer--back">
    <header class="services-header">
      <h1 class="services-header__title">WE CAN<br>HELP YOU<br>WITH...</h1>
    </header>
    <div class="services-panel">
      <div class="column-photo" role="img" aria-label="Black and white photograph of the base of a classical stone column"></div>
      <ul class="service-list">
        <li class="service-list__item">Property Law</li>
        <li class="service-list__item">Conveyancing</li>
        <li class="service-list__item">Leases</li>
        <li class="service-list__item">Criminal Law</li>
        <li class="service-list__item">Family Law</li>
        <li class="service-list__item">Litigation and Dispute Resolution</li>
        <li class="service-list__item">Company Law</li>
        <li class="service-list__item">Wills and Estates</li>
        <li class="service-list__item">Powers of Attorney and Guardianship</li>
      </ul>
    </div>
    <div class="contact-block">
      <p class="firm-name">PRESTWICKS SOLICITORS</p>
      <p class="contact-block__address">3/82 Carradine Street, Liverpool, NSW 2170</p>
      <p class="contact-block__phone">(02) 9418 3562</p>
      <p class="contact-block__link">www.prestwickssolicitors-example.com.au</p>
      <p class="contact-block__link">info@prestwickssolicitors-example.com.au</p>
    </div>
  </section>
</body>
</html>
```